Real Estate Website

We need a web design for a new site that is focused on real estate listings and information for the Singapore, Malaysian and Australian market.

The web site will have listings of available real estate for sale, past transaction data on real estate, information about neighborhoods where the real estate is located.
Website URL will likely be www.havenlotz.com. We are also open to suggestions on site names (assuming URL is available).

We like the simplicity of a similar US site called Pevondo.com - and want to focus on providing a similar "clean" user interface where users can find the information they need. The final design should be user friendly, be visually compelling with a focus on ease of navigation.

Requirements to have at least 5 web pages designed that will display the data as in the attached document for any given territory. We will need to receive
- HTML/CSS/JavaScript, and all images
- any design icons for common objects (e.g. house/home, map, user, agent, trend chart, contact, bathroom, bedroom, garage, furniture, price, ...etc).
Updates

Hi

I just added more details to the brief and committed to pay for the project.
Please review the additional information and submit your final designs by June 14th (or sooner) as we have a deadline to meet. 

Let me know if you have any questions, I will try to be prompt in my responses. 
Thanks.

Target Market(s)

Consumers who are researching real estate to purchase or sell

Industry/Entity Type

Real Estate

Requirements
Must have
• Data in attached document needs to be displayed.

```html
<!DOCTYPE html>
<html lang="en">
<head>
<meta charset="utf-8">
<title>Real Estate</title>
<link rel="stylesheet" href="https://fonts.googleapis.com/css2?family=Didact+Gothic&family=Arimo:wght@400;700&display=swap">
<style>
:root{
  --green:#8fb50e;
  --green-btn:#7aa300;
  --black:#0c0c0c;
  --dark:#2a2a2a;
  --panel:#1b1b1b;
  --text:#c9c9c9;
  --muted:#a5a5a5;
  --white:#ffffff;
  --nav-text:#333333;
}
*{margin:0;padding:0;box-sizing:border-box}
html,body{width:864px;height:1200px;overflow:hidden;background:var(--white)}
body{font-family:"Arimo",Arial,sans-serif;font-size:10.5px;color:var(--text);position:relative}
.page{position:absolute;left:25px;top:0;width:814px;height:1200px}
.heading{font-family:"Didact Gothic",Arial,sans-serif;font-weight:400}
a{color:var(--green);text-decoration:underline}

/* header */
.site-header{position:absolute;left:0;top:0;width:814px;height:77px;background:linear-gradient(#1a1a1a,#000)}
.brand-mark{position:absolute;left:30px;top:22px;width:36px;height:36px;border-radius:50%;background:#8a8a8a}
.brand-name{position:absolute;left:170px;top:14px;font-size:40px;color:var(--white)}
.social{position:absolute;top:26px;width:24px;height:24px;border-radius:5px;background:#1e9bd7}
/* nav */
.main-nav{position:absolute;left:0;top:77px;width:814px;height:62px;background:linear-gradient(#ffffff,#e6e6e6);display:flex}
.main-nav a{flex:1;display:flex;align-items:center;justify-content:center;font-family:"Didact Gothic",Arial,sans-serif;font-size:16px;color:var(--nav-text);text-decoration:none;border-right:1px solid #dcdcdc}
.main-nav a:last-child{border-right:0}
.main-nav a.current{color:var(--green)}

/* hero */
.featured{position:absolute;left:0;top:139px;width:814px;height:568px;background:var(--dark)}
.hero-photo{position:absolute;left:26px;top:17px;width:541px;height:297px;background:linear-gradient(#6f9b4a 0%,#9a5a44 45%,#7d4a3a 70%,#3f5e2b 100%)}
.hero-caption{position:absolute;left:26px;top:251px;width:541px;height:63px;background:rgba(0,0,0,.6);padding:9px 24px}
.hero-caption .title{font-size:21px;color:var(--white)}
.hero-caption .facts{margin-top:6px;font-size:10px;color:var(--white)}
.hero-caption .facts b{color:var(--white)}
.dots{position:absolute;right:24px;bottom:14px;display:flex;gap:4px}
.dots span{width:9px;height:9px;border-radius:50%;background:var(--white)}
.dots span:first-child{background:var(--green)}

.search{position:absolute;left:567px;top:17px;width:220px;height:297px;background:var(--panel);padding:18px 24px}
.search h2{font-size:19px;color:var(--white);padding-bottom:5px;border-bottom:1px solid #777;width:165px}
.search label{display:block;font-size:9.5px;color:var(--muted);margin-top:13px;margin-bottom:2px}
.field{height:16px;background:var(--white);position:relative}
.field.select::after{content:"";position:absolute;right:2px;top:2px;width:12px;height:12px;background:#222}
.row{display:flex;gap:18px}
.row>div{width:74px}
.btn{display:inline-block;background:var(--green-btn);color:var(--white);font-size:10px;padding:5px 14px;border-radius:3px;text-decoration:none}
.search .btn{width:74px;text-align:center;margin-top:13px}
.search .hint{font-size:9.5px;color:var(--muted);margin-top:12px;line-height:16px}

.intro-title{position:absolute;left:49px;top:340px;font-size:29px;color:var(--green)}
.feature{position:absolute;top:385px;width:160px}
.feature .icon{width:40px;height:36px;border-radius:4px;background:linear-gradient(#c9a24c,#b23a22);display:inline-block;vertical-align:middle}
.feature h3{display:inline-block;vertical-align:middle;margin-left:10px;font-size:20px;color:var(--white)}
.feature .lead{margin-top:12px;font-weight:700;color:var(--green);font-size:10px;line-height:17px}
.feature p{margin-top:6px;line-height:16px;font-size:10px;color:var(--text)}
.feature p a{color:var(--white)}
.feature .btn{margin-top:11px}

.offers{position:absolute;left:592px;top:348px}
.offers h2{font-size:20px;color:var(--white);margin-bottom:13px}
.offers li{list-style:none;font-size:10px;line-height:23px;padding-left:12px;position:relative}
.offers li::before{content:"›";position:absolute;left:0;top:-1px;color:var(--white);font-size:13px}

/* remodeling */
.rooms{position:absolute;left:0;top:707px;width:814px;height:389px;background:var(--black)}
.rooms-title{position:absolute;left:49px;top:26px;font-size:29px;color:var(--green)}
.listing{position:absolute;left:51px;width:530px;height:115px}
.listing .photo{position:absolute;left:0;top:0;width:144px;height:115px;background:linear-gradient(#5f9de0,#d9b78a 60%,#4b7a34)}
.listing .body{position:absolute;left:174px;top:1px;width:340px}
.listing .spec{font-weight:700;color:var(--white);font-size:10px}
.listing .price{font-weight:700;color:var(--white);font-size:10px;margin-top:4px}
.listing .price span{color:var(--green)}
.listing p{margin-top:6px;line-height:16px;font-size:10px;color:var(--muted)}
.listing .btn{margin-top:14px}

.news{position:absolute;left:592px;top:36px;width:180px}
.news h2{font-size:20px;color:var(--white);margin-bottom:14px}
.news-item{position:relative;height:96px;padding-left:55px}
.news-date{position:absolute;left:0;top:-6px;width:45px;text-align:center;font-family:"Didact Gothic",Arial,sans-serif;color:var(--green);font-size:37px;line-height:38px}
.news-date small{display:block;font-size:17px;line-height:16px;color:var(--white)}
.news-item a.head{color:var(--white);font-size:10px}
.news-item p{font-size:10px;line-height:16px;color:var(--muted);margin-top:2px}

/* footer */
.site-footer{position:absolute;left:0;top:1096px;width:814px;height:104px;background:linear-gradient(#e9e9e9,#fff 70%)}
.call{position:absolute;right:48px;top:38px;font-size:24px;color:#222}
.call span{color:var(--green)}
</style>
</head>
<body>
<div class="page">
  <header class="site-header">
    <span class="brand-mark"></span>
    <span class="brand-name heading">Real Estate</span>
    <span class="social" style="left:676px"></span>
    <span class="social" style="left:707px"></span>
    <span class="social" style="left:738px"></span>
  </header>

  <nav class="main-nav">
    <a class="current" href="#">Main Page</a>
    <a href="#">Buying Estate</a>
    <a href="#">Selling Estate</a>
    <a href="#">Renting Estate</a>
    <a href="#">Finance</a>
    <a href="#">Contact Us</a>
  </nav>

  <section class="featured">
    <div class="hero-photo" role="img" aria-label="Red brick two-storey house with white trim among green trees"></div>
    <div class="hero-caption">
      <div class="title heading">Villa Neverland, 2006</div>
      <div class="facts">9 rooms, 3 baths, 6 beds, building size: 5000 sq. ft. &nbsp;&nbsp;&nbsp; Price: <b>$ 600 000</b> &nbsp;&nbsp;&nbsp; <a href="#">Read more</a></div>
      <div class="dots"><span></span><span></span><span></span><span></span><span></span></div>
    </div>

    <form class="search">
      <h2 class="heading">Find Your Property</h2>
      <label>City &amp; State, or Zip:</label><div class="field"></div>
      <label>Search Area:</label><div class="field select"></div>
      <div class="row">
        <div><label>Price Range:</label><div class="field select"></div></div>
        <div><label>to:</label><div class="field select"></div></div>
      </div>
      <div class="row">
        <div><label>Bedroom(s):</label><div class="field select"></div></div>
        <div><label>Bathroom(s):</label><div class="field select"></div></div>
      </div>
      <div class="row">
        <div><label>Radius:</label><div class="field select"></div></div>
        <div><a class="btn" href="#">Proposals</a></div>
      </div>
      <p class="hint">Know exactly what you want?<br>Try our <a href="#">Advanced Search</a></p>
    </form>

    <h2 class="intro-title heading">Buyers. Sellers. Proprietors. Agents.</h2>

    <div class="feature" style="left:49px">
      <span class="icon" role="img" aria-label="Small house icon"></span><h3 class="heading">Selling</h3>
      <div class="lead">Welcome one of<br><a href="#">free website templates</a></div>
      <p>created by Stackfold.com team, optimized for 1024x768 px.</p>
      <a class="btn" href="#">Read more</a>
    </div>
    <div class="feature" style="left:224px">
      <span class="icon" role="img" aria-label="Banknotes icon"></span><h3 class="heading">Investing</h3>
      <div class="lead">Free website template for<br>Real Estate business</div>
      <p>goes with PSD source files and without them.</p>
      <a class="btn" href="#">Read more</a>
    </div>
    <div class="feature" style="left:399px">
      <span class="icon" role="img" aria-label="House with sign icon"></span><h3 class="heading">Renting</h3>
      <div class="lead">Template has several pages</div>
      <p><a href="#">Main</a>, <a href="#">Buying</a>, <a href="#">Selling</a>, <a href="#">Renting</a>, <a href="#">Finance</a>, <a href="#">Contacts</a> (note that contact us form – doesn't work).</p>
      <a class="btn" href="#">Read more</a>
    </div>

    <aside class="offers">
      <h2 class="heading">Special Offers</h2>
      <ul>
        <li><a href="#">Home Loan Offer</a></li>
        <li><a href="#">Free Calculators</a></li>
        <li><a href="#">Free Loan Tools</a></li>
        <li><a href="#">Value Your Home</a></li>
        <li><a href="#">Recently Sold Properties</a></li>
        <li><a href="#">Suburb Statistics</a></li>
        <li><a href="#">Compare Property Prices</a></li>
      </ul>
    </aside>
  </section>

  <section class="rooms">
    <h2 class="rooms-title heading">Remodeling Rooms</h2>

    <article class="listing" style="top:81px">
      <div class="photo" role="img" aria-label="Cream villa with red roof under blue sky"></div>
      <div class="body">
        <div class="spec">2006, 3 baths, 6 beds, building size: 5000 sq. ft.</div>
        <div class="price">Price: <span>$ 600 000</span></div>
        <p>Massa dictum ementum velitumo od consequat ante oremsumas ame consectetueraipiscing eliteli ueedlorAliquam conguen nisauris accusalla vel deinol tincidunt ligula magna semper ipsum.</p>
        <a class="btn" href="#">Read more</a>
      </div>
    </article>

    <article class="listing" style="top:228px">
      <div class="photo" role="img" aria-label="Modern white and wood house with palm garden"></div>
      <div class="body">
        <div class="spec">2006, 3 baths, 6 beds, building size: 5000 sq. ft.</div>
        <div class="price">Price: <span>$ 600 000</span></div>
        <p>Massa dictum ementum velitumo od consequat ante oremsumas ame consectetueraipiscing eliteli ueedlorAliquam conguen nisauris accusalla vel deinol tincidunt ligula magna semper ipsum.</p>
        <a class="btn" href="#">Read more</a>
      </div>
    </article>

    <aside class="news">
      <h2 class="heading">Recent News</h2>
      <div class="news-item">
        <div class="news-date">28<small>may</small></div>
        <a class="head" href="#">Donec consequat risus</a>
        <p>Hendrerit conghdim entum diam metus fringilla nisl, in porta sapien purus quis odiosem... <a href="#">more</a></p>
      </div>
      <div class="news-item">
        <div class="news-date">25<small>may</small></div>
        <a class="head" href="#">Nullam dignissim</a>
        <p>Laoreet neque, quis sollic-itudin orci tempus etiam viverra leo euismod pulvi-nar accumsan... <a href="#">more</a></p>
      </div>
      <div class="news-item">
        <div class="news-date">22<small>may</small></div>
        <a class="head" href="#">Quisque nunc lorem</a>
        <p>Feugiat nec sodales quis, iaculis sed libero. Cras vel nisl justo, ac posuere est nulla facilisi... <a href="#">more</a></p>
      </div>
    </aside>
  </section>

  <footer class="site-footer">
    <div class="call heading"><span>Call Center:</span> 1-800-555-0142</div>
  </footer>
</div>
</body>
</html>
```